Killer business card for bowling event and marketing company

Strike Line Promotions is a sports marketing company that specializes in unique bowling events that provide return on investment for sponsors and memorable experiences for participants and spectators. We need a new business card that simultaneously communicates professionalism and fun. Our preferred colors are black and re

Target Market(s)

Executives in the marketing and sponsorship departments of companies, tourism executives, bowling center owners, and people who love to bowl.

Industry/Entity Type

Business

Contact Information for Business Card

Dean T Walsh
Strike Line Promotions
PO Box 47
Fairhaven, Ohio USA 44871
Email: deant@strikelinepromotions.com
Mobile: 1-555-518-3762

Requirements
Must have
• Our preferred colors are black and red.
Nice to have
• I am considering the use of the attached image for the back of the card.

```html
<!DOCTYPE html>
<html lang="en">
<head>
<meta charset="utf-8">
<title>Strike Line Promotions – Business Card</title>
<link rel="stylesheet" href="https://fonts.googleapis.com/css2?family=Oswald:wght@600&family=Arimo:wght@400;700&display=swap">
<style>
  :root {
    --card-black: #000000;
    --brand-red: #d9161c;
    --deep-red: #8e0b0f;
    --text-white: #ffffff;
    --display-font: "Oswald", sans-serif;
    --body-font: "Arimo", sans-serif;
  }
  html, body {
    margin: 0;
    padding: 0;
    overflow: hidden;
    background: var(--card-black);
  }
  .card {
    position: relative;
    width: 1200px;
    height: 666px;
    background: var(--card-black);
    overflow: hidden;
    font-family: var(--body-font);
  }
  .top-rule {
    position: absolute;
    top: 0;
    left: 90px;
    width: 1010px;
    height: 14px;
    background: linear-gradient(90deg, transparent 0%, var(--deep-red) 20%, var(--brand-red) 55%, var(--deep-red) 85%, transparent 100%);
  }
  .brand-mark {
    position: absolute;
    top: 98px;
    left: 176px;
    width: 110px;
    height: 110px;
    border-radius: 50%;
    background: var(--brand-red);
  }
  .brand-divider {
    position: absolute;
    top: 76px;
    left: 348px;
    width: 4px;
    height: 150px;
    background: var(--brand-red);
  }
  .brand-name {
    position: absolute;
    top: 92px;
    left: 382px;
    margin: 0;
    font-family: var(--body-font);
    font-weight: 700;
    font-size: 56px;
    line-height: 62px;
    color: var(--text-white);
  }
  .name-band {
    position: absolute;
    top: 386px;
    left: 0;
    width: 60px;
    height: 146px;
    background: linear-gradient(90deg, var(--brand-red) 0%, var(--deep-red) 100%);
  }
  .holder {
    position: absolute;
    top: 396px;
    left: 71px;
  }
  .holder-name {
    margin: 0;
    font-family: var(--display-font);
    font-weight: 600;
    font-size: 70px;
    line-height: 1;
    letter-spacing: 1px;
    color: var(--text-white);
    transform: scaleX(0.94);
    transform-origin: left;
  }
  .holder-company {
    margin: 8px 0 0 2px;
    font-weight: 700;
    font-size: 34px;
    line-height: 1;
    color: var(--brand-red);
  }
  .contact-list {
    position: absolute;
    top: 388px;
    left: 648px;
    margin: 0;
    padding: 0;
    list-style: none;
  }
  .contact-item {
    display: flex;
    align-items: flex-start;
    gap: 22px;
    font-size: 29px;
    line-height: 33px;
    color: var(--text-white);
    margin-bottom: 30px;
  }
  .contact-item.address { margin-bottom: 22px; }
  .contact-icon {
    flex: none;
    width: 40px;
    height: 40px;
  }
  .address .contact-icon { margin-top: 10px; }
</style>
</head>
<body>
<div class="card">
  <div class="top-rule"></div>

  <span class="brand-mark"></span>
  <span class="brand-divider"></span>
  <p class="brand-name">Strike Line<br>Promotions</p>

  <div class="name-band"></div>
  <div class="holder">
    <h1 class="holder-name">DEAN T. WALSH</h1>
    <p class="holder-company">Strike Line Promotions</p>
  </div>

  <ul class="contact-list">
    <li class="contact-item address">
      <svg class="contact-icon" viewBox="0 0 40 40" aria-hidden="true">
        <path d="M20 4c-6 0-10.5 4.5-10.5 10.3C9.5 21.5 20 32 20 32s10.5-10.5 10.5-17.7C30.5 8.5 26 4 20 4z" fill="var(--brand-red)"/>
        <circle cx="20" cy="14.5" r="4" fill="var(--card-black)"/>
        <ellipse cx="20" cy="34.5" rx="10" ry="3" fill="none" stroke="var(--brand-red)" stroke-width="2.5"/>
      </svg>
      <span>PO Box 47<br>Fairhaven, Ohio USA 44871</span>
    </li>
    <li class="contact-item email">
      <svg class="contact-icon" viewBox="0 0 40 40" aria-hidden="true">
        <rect x="2" y="8" width="36" height="24" fill="var(--brand-red)"/>
        <path d="M3 9l17 13L37 9" fill="none" stroke="var(--card-black)" stroke-width="2.5"/>
      </svg>
      <span>deant@strikelinepromotions.com</span>
    </li>
    <li class="contact-item phone">
      <svg class="contact-icon" viewBox="0 0 40 40" aria-hidden="true">
        <rect x="10" y="2" width="20" height="36" rx="3" fill="none" stroke="var(--brand-red)" stroke-width="3"/>
        <line x1="17" y1="33" x2="23" y2="33" stroke="var(--brand-red)" stroke-width="2.5"/>
      </svg>
      <span>1-555-518-3762</span>
    </li>
  </ul>
</div>
</body>
</html>
```